Business card for Chiropractic clinics needs reworked / redesigned

The business card in attachment was designed 10 years ago. It is in need of an update.
We have 2 clinics:
VELDHOVE KLINIEK & VELDHOVE KLINIEK NOORD
Only one address needs to be on the card for doctors that only work in one clinic and two addresses need to be on the card for the doctors that work in both clinics.

Target Market(s)

patients/referrers

Industry/Entity Type

Medical

Contact Information for Business Card

Logo (in full or zoomed-in)
Clinic Name
Doctor name and title
clinic address, website, tel, email

Font styles to use
Sans Serif

Colors

Designer to choose colors to be used in the design.

Requirements
Must have
• Good contrast/readability
• We like modern minimalistic designs
• The Bcard needs to project our very high standard of proficiency/professionalism
Should not have
• Not curly
• Not to much colours

```html
<!DOCTYPE html>
<html lang="en">
<head>
<meta charset="utf-8">
<title>Veldhove Kliniek – Business Card</title>
<link rel="stylesheet" href="https://fonts.googleapis.com/css2?family=Lato:wght@300;400;700&display=swap">
<style>
  :root {
    --ink: #1b2526;
    --brand-dark: #0c2a2c;
    --paper: #ffffff;
    --stage: #e6e8e8;
    --faint: #d9dcdc;
  }
  * { box-sizing: border-box; margin: 0; padding: 0; }
  html, body { width: 1200px; height: 782px; overflow: hidden; }
  body {
    background: var(--stage);
    font-family: "Lato", sans-serif;
    color: var(--ink);
    display: flex;
    align-items: center;
    justify-content: center;
    gap: 40px;
  }
  .card {
    width: 560px;
    height: 320px;
    position: relative;
    overflow: hidden;
    box-shadow: 0 6px 18px rgba(0,0,0,.18);
  }
  .card--front { background: var(--paper); }
  .card--back {
    background: var(--brand-dark);
    display: flex;
    align-items: center;
    justify-content: center;
  }
  .brand-mark {
    display: flex;
    align-items: center;
    gap: 12px;
    color: var(--paper);
    font-weight: 400;
    font-size: 20px;
    letter-spacing: 3px;
  }
  .brand-mark__dot {
    width: 12px; height: 12px;
    border-radius: 50%;
    background: var(--paper);
  }
  .doctor { position: absolute; left: 34px; top: 30px; }
  .doctor__name { font-weight: 700; font-size: 17px; letter-spacing: .4px; }
  .doctor__title { font-weight: 300; font-size: 13px; letter-spacing: 1px; margin-top: 2px; }
  .clinic { position: absolute; font-size: 12.5px; line-height: 1.45; }
  .clinic--main { left: 34px; top: 96px; }
  .clinic--second { left: 300px; top: 150px; }
  .clinic__name { font-weight: 700; font-size: 12.5px; letter-spacing: .3px; }
  .clinic__line { display: flex; align-items: center; gap: 6px; }
  .clinic__line svg { width: 11px; height: 11px; flex: none; fill: var(--ink); }
  .faint-name {
    position: absolute;
    right: 26px; top: 120px;
    color: var(--faint);
    font-weight: 400;
    font-size: 15px;
    letter-spacing: 3px;
  }
  .wave { position: absolute; left: 0; bottom: 0; width: 560px; height: 140px; }
</style>
</head>
<body>
  <section class="card card--front" aria-label="Business card front">
    <span class="faint-name">VELDHOVE KLINIEK</span>

    <div class="doctor">
      <p class="doctor__name">MAARTEN VERLINDE</p>
      <p class="doctor__title">CHIROPRACTOR</p>
    </div>

    <div class="clinic clinic--main">
      <p class="clinic__name">VELDHOVE KLINIEK</p>
      <p>Lindenlaan 48</p>
      <p class="clinic__line"><svg viewBox="0 0 12 12"><path d="M2 1h3l1 3-2 1a7 7 0 0 0 3 3l1-2 3 1v3a1 1 0 0 1-1 1A10 10 0 0 1 1 2a1 1 0 0 1 1-1z"/></svg>09 555 01 42</p>
      <p class="clinic__line"><svg viewBox="0 0 12 12"><path d="M1 2.5h10v7H1z M1 2.5l5 4 5-4" fill="none" stroke="#1b2526" stroke-width="1.2"/></svg>info@veldhovekliniek.be</p>
      <p class="clinic__line"><svg viewBox="0 0 12 12"><circle cx="6" cy="6" r="5"/></svg>www.veldhovekliniek.be</p>
    </div>

    <div class="clinic clinic--second">
      <p class="clinic__name">VELDHOVE KLINIEK NOORD</p>
      <p>Kerkstraat 17</p>
      <p class="clinic__line"><svg viewBox="0 0 12 12"><path d="M2 1h3l1 3-2 1a7 7 0 0 0 3 3l1-2 3 1v3a1 1 0 0 1-1 1A10 10 0 0 1 1 2a1 1 0 0 1 1-1z"/></svg>09 555 08 27</p>
      <p class="clinic__line"><svg viewBox="0 0 12 12"><circle cx="6" cy="6" r="5"/></svg>veldhovekliniek-noord.be</p>
    </div>

    <svg class="wave" viewBox="0 0 560 140" preserveAspectRatio="none" aria-hidden="true">
      <path d="M0 28 C120 60 260 110 400 112 C470 114 530 120 560 126 L560 140 L0 140 Z" fill="var(--brand-dark)"/>
      <path d="M0 8 C110 40 240 86 370 96 C440 100 520 106 560 104" fill="none" stroke="var(--brand-dark)" stroke-width="16"/>
      <path d="M0 22 C120 54 260 104 400 106 C470 108 530 114 560 120" fill="none" stroke="var(--paper)" stroke-width="3"/>
    </svg>
  </section>

  <section class="card card--back" aria-label="Business card back">
    <div class="brand-mark">
      <span class="brand-mark__dot"></span>
      <span>VELDHOVE KLINIEK</span>
    </div>
  </section>
</body>
</html>
```